Design for Certificate

Design a certificate for training, providing our company logo such as attachments. Company's name is "BRYNE Fjellvik Advisory Ltd", please refer to our company profile: https://www.bryne-fjellvik.example/company_info

The style of the current certificate is also attached, and another certificate of another company can be referred to. Psd & jpg are required for the final draft (the layers of psd are not merged). Thanks!

```html
<!DOCTYPE html>
<html lang="en">
<head>
<meta charset="utf-8">
<title>Certificate of Completion – BRYNE Fjellvik Advisory Ltd</title>
<link rel="stylesheet" href="https://fonts.googleapis.com/css2?family=Montserrat:wght@500;600;700&family=Libre+Bodoni:ital@1&display=swap">
<style>
  :root {
    --paper: #fdfdf9;
    --pattern: #f7f6ea;
    --charcoal: #383b3c;
    --peach: #e0bb9c;
    --ink: #555657;
    --gold-light: #fff3b0;
    --gold: #e5c454;
    --gold-deep: #d4b34a;
    --title-top: #e7d48a;
    --title-bottom: #a07d5e;
  }
  html, body {
    margin: 0;
    padding: 0;
    width: 1200px;
    height: 848px;
    overflow: hidden;
    background: var(--paper);
  }
  .certificate {
    position: relative;
    width: 1200px;
    height: 848px;
    display: block;
  }
  .sans { font-family: "Montserrat", Arial, sans-serif; }
  .serif-italic { font-family: "Libre Bodoni", "Bodoni Moda", Georgia, serif; font-style: italic; }
  .cert-number-label { fill: var(--peach); font-weight: 600; font-size: 21px; letter-spacing: 1px; }
  .title-main { font-weight: 700; font-size: 82px; letter-spacing: 5px; }
  .title-sub { font-weight: 700; font-size: 27px; letter-spacing: 5px; }
  .awarded-line { fill: var(--ink); font-size: 28px; letter-spacing: 2px; }
  .completed-line { fill: var(--ink); font-size: 24px; letter-spacing: 1px; }
  .course-name { font-weight: 700; font-size: 23.5px; letter-spacing: 1.2px; }
  .course-topic { fill: var(--peach); }
  .course-type { fill: var(--ink); }
  .course-hours { fill: var(--peach); font-weight: 700; font-size: 23.5px; letter-spacing: 1.2px; }
  .field-label { fill: var(--ink); font-weight: 500; font-size: 24px; letter-spacing: 3.5px; }
  .seal-name { fill: var(--peach); font-weight: 600; font-size: 22px; letter-spacing: 2px; }
  .fill-line { stroke: var(--charcoal); stroke-width: 1.4; }
  .frame-line { fill: none; stroke: url(#frameGold); stroke-width: 2.4; }
</style>
</head>
<body>
<svg class="certificate" viewBox="0 0 1200 848" xmlns="http://www.w3.org/2000/svg">
  <defs>
    <linearGradient id="cornerGold" x1="0" y1="0" x2="1" y2="1">
      <stop offset="0" stop-color="#f5e2a0"/>
      <stop offset="0.5" stop-color="#fff6cf"/>
      <stop offset="1" stop-color="#efdca0"/>
    </linearGradient>
    <linearGradient id="frameGold" x1="0" y1="0" x2="1" y2="1">
      <stop offset="0" stop-color="var(--gold-light)"/>
      <stop offset="0.5" stop-color="var(--gold)"/>
      <stop offset="1" stop-color="var(--gold-deep)"/>
    </linearGradient>
    <linearGradient id="titleGold" x1="0" y1="0" x2="0" y2="1">
      <stop offset="0" stop-color="var(--title-top)"/>
      <stop offset="1" stop-color="var(--title-bottom)"/>
    </linearGradient>
  </defs>

  <!-- background field -->
  <rect class="background-pattern" width="1200" height="848" fill="var(--pattern)" opacity="0.45" role="img" aria-label="Faint geometric star pattern across the certificate background"/>

  <!-- top-left corner -->
  <g class="corner corner-top-left">
    <polygon points="0,0 230,0 230,150 0,298" fill="url(#cornerGold)"/>
    <polygon points="18,0 549,0 274,189" fill="var(--peach)"/>
    <polygon points="63,0 489,0 274,149" fill="var(--charcoal)"/>
  </g>

  <!-- bottom-right corner -->
  <g class="corner corner-bottom-right">
    <polygon points="985,698 1200,549 1200,848 1090,848" fill="url(#cornerGold)"/>
    <polygon points="648,848 925,657 1200,845 1200,848" fill="var(--peach)"/>
    <polygon points="726,848 925,709 1124,848" fill="var(--charcoal)"/>
  </g>

  <!-- gold frames -->
  <g class="frame">
    <polyline class="frame-line" points="539,57.5 1145,57.5 1145,502"/>
    <polyline class="frame-line" points="519,77.5 1125,77.5 1125,521"/>
    <polyline class="frame-line" points="69.5,332 69.5,781 679,781"/>
    <polyline class="frame-line" points="50,352 50,800 659,800"/>
  </g>

  <!-- certificate number -->
  <g class="cert-number">
    <text class="sans cert-number-label" x="723" y="131">Certificate No:</text>
    <line x1="921" y1="131" x2="1093" y2="131" stroke="#6b6b6b" stroke-width="1.2"/>
  </g>

  <!-- title -->
  <text class="sans title-main" x="593" y="266" text-anchor="middle" fill="url(#titleGold)">CERTIFICATE</text>
  <text class="sans title-sub" x="600" y="310" text-anchor="middle" fill="url(#titleGold)">OF COMPLETION</text>

  <!-- recipient -->
  <text class="serif-italic awarded-line" x="594" y="377" text-anchor="middle">This Certificate is awarded to</text>
  <line class="fill-line recipient-line" x1="219" y1="469" x2="996" y2="469"/>
  <text class="serif-italic completed-line" x="604" y="523" text-anchor="middle">has successfully completed</text>

  <!-- course -->
  <text class="sans course-name" x="124" y="593" textLength="715" lengthAdjust="spacing"><tspan class="course-topic">BRAND REPUTATION MANAGEMENT</tspan> <tspan class="course-type">TRAINING COURSE</tspan></text>
  <line x1="855.5" y1="550" x2="855.5" y2="617" stroke="var(--ink)" stroke-width="1"/>
  <text class="sans course-hours" x="870" y="593">16HOURS</text>

  <!-- date / seal / signature -->
  <line class="fill-line" x1="131" y1="695" x2="387" y2="695"/>
  <text class="sans field-label" x="251" y="733" text-anchor="middle">DATE</text>

  <g class="company-seal">
    <circle cx="480" cy="696" r="62" fill="var(--charcoal)"/>
    <text class="sans seal-name" x="481" y="704" text-anchor="middle">BRYNE</text>
  </g>

  <line class="fill-line" x1="575" y1="695" x2="840" y2="695"/>
  <text class="sans field-label" x="689" y="733" text-anchor="middle">SIGNATURE</text>
</svg>
</body>
</html>
```